Business Card Design

This is a coaching and training company. We deliver personal development workshops, training and one to one coaching. We would like the current logo to be used.

Target Market(s)

For coaches, small business owners and people aged around 40-60 who are seeking direction in their life

Industry/Entity Type

Training

Contact Information for Business Card

Moira Treadwell
Speaker-Trainer-Coach
There is no going back ...
0461 839205
18 Pellow Road Marbury
motread47@quillnet.example

Font styles to use
Sans Serif

Requirements
Should not have
• No old style fonts

```html
<!DOCTYPE html>
<html lang="en">
<head>
<meta charset="utf-8">
<title>Crossway Business Card</title>
<link rel="stylesheet" href="https://fonts.googleapis.com/css2?family=Arimo:wght@400;700&family=Montserrat:wght@600&display=swap">
<style>
  :root {
    --backdrop: #808184;
    --card-white: #ffffff;
    --brand-blue: #1b9cc9;
    --deep-blue: #3b7594;
    --wing-light: #4fa8cf;
    --ink-grey: #555b60;
    --rule-grey: #9a9ea2;
    --box-light: #f1f2f3;
    --box-mid: #d4d6d8;
    --curve-shadow: #c9cccf;
  }
  * { margin: 0; padding: 0; box-sizing: border-box; }
  html, body { width: 1200px; height: 1200px; overflow: hidden; }
  body {
    background: var(--backdrop);
    font-family: "Arimo", Arial, sans-serif;
    position: relative;
  }
  .card {
    position: absolute;
    left: 121px;
    width: 960px;
    height: 590px;
    background: var(--card-white);
    overflow: hidden;
  }
  .card--front { top: 6px; }
  .card--back { top: 606px; }

  .wing {
    position: absolute;
    top: 0;
    width: 240px;
    height: 590px;
  }
  .wing--left { left: 0; }
  .wing--right { right: 0; }

  .brand {
    position: absolute;
    display: flex;
    flex-direction: column;
    align-items: center;
  }
  .brand__square {
    background: linear-gradient(135deg, var(--box-light), var(--box-mid));
  }
  .brand__name {
    font-family: "Arimo", Arial, sans-serif;
    font-weight: 400;
    color: var(--brand-blue);
    letter-spacing: 1px;
    line-height: 1;
  }
  .brand__rule {
    height: 1px;
    background: var(--rule-grey);
  }
  .brand__tagline {
    color: var(--ink-grey);
    line-height: 1;
  }

  .card--front .brand { left: 0; right: 0; top: 36px; }
  .card--front .brand__square { width: 340px; height: 290px; }
  .card--front .brand__name { font-size: 60px; margin-top: 22px; }
  .card--front .brand__rule { width: 340px; margin-top: 12px; }
  .card--front .brand__tagline { font-size: 23px; margin-top: 8px; }

  .person {
    position: absolute;
    left: 0; right: 0;
    top: 468px;
    text-align: center;
  }
  .person__name {
    font-size: 38px;
    color: var(--brand-blue);
    text-decoration: underline;
    text-underline-offset: 5px;
    text-decoration-thickness: 2px;
  }
  .person__role {
    margin-top: 14px;
    font-size: 26px;
    color: var(--ink-grey);
  }

  .back-panel {
    position: absolute;
    inset: 0;
    width: 960px;
    height: 590px;
  }
  .motto {
    position: absolute;
    left: 107px;
    top: 104px;
    font-family: "Montserrat", Arial, sans-serif;
    font-weight: 600;
    font-size: 60px;
    line-height: 70px;
    color: var(--card-white);
    letter-spacing: 1px;
  }
  .contact {
    position: absolute;
    left: 89px;
    top: 460px;
    color: var(--card-white);
    font-size: 19px;
    line-height: 30px;
    list-style: none;
  }
  .card--back .brand { left: 584px; top: 154px; width: 264px; }
  .card--back .brand__square { width: 264px; height: 214px; }
  .card--back .brand__name { font-size: 50px; margin-top: 26px; }
  .card--back .brand__rule { width: 264px; margin-top: 8px; }
  .card--back .brand__tagline { font-size: 17px; margin-top: 6px; }
</style>
</head>
<body>

<section class="card card--front">
  <svg class="wing wing--left" viewBox="0 0 240 590" role="img" aria-label="Feathered blue wing strokes sweeping inward">
    <defs>
      <linearGradient id="wingLeftFill" x1="0" y1="0" x2="0.4" y2="1">
        <stop offset="0" stop-color="#3b7594"/>
        <stop offset="1" stop-color="#4fa8cf"/>
      </linearGradient>
    </defs>
    <polygon points="0,0 120,0 220,420 0,560" fill="url(#wingLeftFill)" opacity="0.85"/>
  </svg>
  <svg class="wing wing--right" viewBox="0 0 240 590" role="img" aria-label="Feathered blue wing strokes sweeping inward">
    <defs>
      <linearGradient id="wingRightFill" x1="1" y1="0" x2="0.6" y2="1">
        <stop offset="0" stop-color="#3b7594"/>
        <stop offset="1" stop-color="#4fa8cf"/>
      </linearGradient>
    </defs>
    <polygon points="240,0 120,0 20,420 240,560" fill="url(#wingRightFill)" opacity="0.85"/>
  </svg>

  <div class="brand">
    <div class="brand__square"></div>
    <div class="brand__name">CROSSWAY</div>
    <div class="brand__rule"></div>
    <div class="brand__tagline">Coaching and Training Solutions</div>
  </div>

  <div class="person">
    <div class="person__name">Moira Treadwell</div>
    <div class="person__role">Speaker-Trainer-Coach</div>
  </div>
</section>

<section class="card card--back">
  <svg class="back-panel" viewBox="0 0 960 590" aria-hidden="true">
    <path d="M527 0 C610 80 570 200 480 300 C405 390 430 520 775 590 L760 590 C415 520 392 390 468 300 C556 200 596 80 510 0 Z" fill="var(--curve-shadow)"/>
    <path d="M0 0 L510 0 C596 80 556 200 468 300 C392 390 415 520 760 590 L0 590 Z" fill="var(--brand-blue)"/>
  </svg>

  <h1 class="motto">THERE<br>IS NO<br>GOING<br>BACK</h1>

  <ul class="contact">
    <li>FIND US at 18 Pellow Road Marbury</li>
    <li>tel: 0461 839205</li>
    <li>email: motread47@quillnet.example</li>
  </ul>

  <div class="brand">
    <div class="brand__square"></div>
    <div class="brand__name">CROSSWAY</div>
    <div class="brand__rule"></div>
    <div class="brand__tagline">Coaching and Training Solutions</div>
  </div>
</section>

</body>
</html>
```